Book Cover Design Project

I have written a booK called "Build From Nothing:
a handbook for launching and steering a modest enterprise. It is aimed at the start up entrepreneur and seeks to give them everything they need to start up and run a small business. I am interested in a very simple cover that is contemporary in the look but clearly communicates the mission of the book. It should sell very well as there are no others like it, so the designer will get excellent exposure.
Updates

Reason: I an vacation in Europe until the 23rd of July. Would like a few days to make a decision after my return Ned

We are currently on vacation.  Will make a final decision in about a week.  Thanks so much for your submissions

Ned

Target Market(s)

Start up businesses in the U.S.

Industry/Entity Type

Business

Requirements
Must have
• Clear communication of the name. Lots of white space. Graphic communication of the purpose of the book? Prominent exposure of my name. Edward r. Kistlewood

```html
<!DOCTYPE html>
<html lang="en">
<head>
<meta charset="utf-8">
<title>Build From Nothing – Cover Layout</title>
<link rel="stylesheet" href="https://fonts.googleapis.com/css2?family=Anton&family=Arimo:ital,wght@0,400;0,700;1,700&display=swap">
<style>
  :root {
    --stage: #f7f9fa;
    --paper: #ffffff;
    --cyan: #4dd7fd;
    --ink: #000000;
    --white: #ffffff;
    --mark: #dde0e2;
    --fold: #eceff1;
  }
  * { margin: 0; padding: 0; box-sizing: border-box; }
  html, body { width: 1200px; height: 900px; overflow: hidden; background: var(--stage); }
  .stage { position: relative; width: 1200px; height: 900px; font-family: "Arimo", Arial, sans-serif; }

  .panel { position: absolute; top: 126px; height: 648px; background: var(--paper); }
  .back-cover { left: 138px; width: 432px; }
  .spine { left: 570px; width: 58px; border-left: 2px solid var(--fold); border-right: 2px solid var(--fold); }
  .front-cover { left: 628px; width: 432px; }

  .rule { position: absolute; left: 0; width: 100%; height: 2px; background: var(--cyan); }
  .rule--top { top: 62px; }
  .rule--bottom { top: 564px; }

  .crop-marks { position: absolute; inset: 0; pointer-events: none; }

  /* back */
  .blurb { position: absolute; left: 84px; top: 105px; width: 265px; }
  .blurb__heading {
    height: 83px; background: var(--cyan); display: flex; align-items: center; justify-content: center;
    font-weight: 700; font-size: 21px; color: var(--ink); letter-spacing: -0.2px;
  }
  .blurb__body {
    margin-top: 2px; height: 211px; background: var(--cyan); padding: 22px 15px 0 16px;
    color: var(--white); font-size: 13.4px; line-height: 14.9px; text-align: justify; hyphens: manual;
  }

  /* spine */
  .spine__author, .spine__title {
    position: absolute; left: 50%; writing-mode: vertical-rl; transform: translateX(-50%); white-space: nowrap;
  }
  .spine__author { top: 132px; font-weight: 700; font-size: 16px; color: var(--ink); }
  .spine__title { top: 348px; font-family: "Anton", Impact, sans-serif; font-size: 19px; color: var(--cyan); letter-spacing: 0.5px; }

  /* front */
  .tagline-box {
    position: absolute; left: 84px; top: 105px; width: 265px; height: 83px; background: var(--cyan);
    display: flex; align-items: center; justify-content: center;
  }
  .tagline { font-weight: 700; font-size: 14.5px; line-height: 19px; color: var(--ink); width: 200px; }
  .tagline em { color: var(--white); font-style: italic; }

  .title-block {
    position: absolute; left: 84px; top: 190px; width: 265px; height: 333px; background: var(--cyan); overflow: visible;
  }
  .title { font-family: "Anton", Impact, sans-serif; font-weight: 400; text-transform: uppercase; line-height: 1; }
  .title__line { display: block; position: absolute; left: 4px; }
  .title__line--1 { top: 8px; font-size: 112px; color: var(--ink); letter-spacing: -1px; }
  .title__line--2 { top: 112px; font-size: 112px; color: var(--ink); letter-spacing: -1px; }
  .title__line--3 { top: 228px; font-size: 84px; color: var(--white); letter-spacing: -1px; }

  .author-box {
    position: absolute; left: 84px; top: 544px; width: 265px; height: 42px; background: var(--cyan);
    display: flex; align-items: center; justify-content: center;
    font-weight: 700; font-size: 17px; color: var(--white);
  }
</style>
</head>
<body>
<main class="stage">
  <section class="panel back-cover">
    <div class="rule rule--top"></div>
    <div class="rule rule--bottom"></div>
    <div class="blurb">
      <h2 class="blurb__heading">Lorem Ipsum Dolor</h2>
      <p class="blurb__body">Lorem ipsum dolor sit amet, consec­tetuer adipiscing elit, sed diam non­ummy nibh euismod tincidunt ut lao­reet dolore magna aliquam erat volutpat. Ut wisi enim ad minim veniam, quis nostrud exerci tation ullamcorper suscipit lobortis nisl ut aliquip ex ea commodo consequat. Duis autem vel eum iriure dolor in hendrerit in vulputate velit esse mo­</p>
    </div>
  </section>

  <section class="panel spine">
    <span class="spine__author">Edward r. Kistlewood</span>
    <span class="spine__title">BUILD FROM NOTHING</span>
  </section>

  <section class="panel front-cover">
    <div class="rule rule--top"></div>
    <div class="rule rule--bottom"></div>
    <div class="tagline-box">
      <p class="tagline">a handbook for <em>launching and steering a modest enterprise</em></p>
    </div>
    <div class="title-block">
      <h1 class="title">
        <span class="title__line title__line--1">Build</span>
        <span class="title__line title__line--2">From</span>
        <span class="title__line title__line--3">Nothing</span>
      </h1>
    </div>
    <p class="author-box">Edward r. Kistlewood</p>
  </section>

  <svg class="crop-marks" width="1200" height="900" viewBox="0 0 1200 900" aria-hidden="true">
    <g stroke="var(--mark)" stroke-width="3" fill="none">
      <path d="M137 106v40M117 126h40"/>
      <path d="M571 106v40M551 126h40"/>
      <path d="M626 106v40M606 126h40"/>
      <path d="M1061 106v40M1041 126h40"/>
      <path d="M137 754v40M117 774h40"/>
      <path d="M571 754v40M551 774h40"/>
      <path d="M626 754v40M606 774h40"/>
      <path d="M1061 754v40M1041 774h40"/>
    </g>
  </svg>
</main>
</body>
</html>
```